Birchwood Clover Business Cards

I need a business card with my logo, number, Facebook account, and some information about what I am selling. Green card with logo on the front. 555-218-3946 phone number, @birchwoodclover Facebook, •Orchardgrass Hay •Alfalfa Hay •Mixed Grass Hay , and “Premium Quality Hay” all written on the back.

Target Market(s)

Hay

Contact Information for Business Card

Phone number, Facebook, different types of hay.

Colors
00AB8E
00BBA5
67D7C9
C6EFE9
E9F9F6

```html
<!DOCTYPE html>
<html lang="en">
<head>
<meta charset="utf-8">
<title>Birchwood Clover Business Cards</title>
<link rel="stylesheet" href="https://fonts.googleapis.com/css2?family=Arimo:wght@400;700&family=Kaushan+Script&display=swap">
<style>
  :root {
    --page-bg: #e4e4e2;
    --card-white: #f6f6f4;
    --card-dark: #2a2b2e;
    --brand-green: #00a14b;
    --soft-green: #cfe9d8;
    --ink: #2b2b2b;
    --ink-light: #d9d9d9;
  }
  * { margin: 0; padding: 0; box-sizing: border-box; }
  html, body {
    width: 1200px; height: 801px; overflow: hidden;
    background: var(--page-bg);
    font-family: "Arimo", Arial, sans-serif;
  }
  .canvas {
    position: relative; width: 1200px; height: 801px;
    display: flex; align-items: center; justify-content: center; gap: 48px;
  }
  .card {
    position: relative; width: 530px; height: 303px;
    border-bottom: 5px solid var(--brand-green);
    box-shadow: 0 14px 30px rgba(0,0,0,0.18);
    overflow: hidden;
  }
  /* Front */
  .card--front { background: var(--card-white); }
  .front__decor {
    position: absolute; right: 40px; top: 70px;
    width: 190px; height: 190px; border-radius: 50%;
    background: var(--soft-green); opacity: 0.55;
  }
  .front__person {
    position: absolute; right: 46px; top: 30px; text-align: right;
  }
  .person__name {
    font-family: "Kaushan Script", cursive;
    color: var(--brand-green); font-size: 34px; line-height: 1;
  }
  .person__role {
    font-size: 15px; color: var(--ink); margin-top: 4px;
  }
  .front__brand {
    position: absolute; left: 36px; bottom: 40px;
    display: flex; align-items: center; gap: 18px;
  }
  .brand-dot {
    width: 62px; height: 62px; border-radius: 50%;
    background: var(--brand-green); flex: none;
  }
  .brand-name {
    font-weight: 700; font-size: 26px; color: var(--ink); line-height: 1;
  }
  .contact-list { list-style: none; margin-top: 12px; }
  .contact-list li {
    display: flex; align-items: center; gap: 9px;
    font-size: 15px; color: var(--ink); margin-top: 5px;
  }
  .contact-icon { width: 14px; height: 14px; flex: none; }
  .contact-square {
    width: 13px; height: 13px; border-radius: 2px;
    background: var(--brand-green); flex: none;
  }
  /* Back */
  .card--back { background: var(--card-dark); }
  .back__brand {
    position: absolute; left: 0; right: 0; top: 92px;
    display: flex; align-items: center; justify-content: center; gap: 20px;
  }
  .back__brand .brand-dot { width: 78px; height: 78px; }
  .back__brand .brand-name { color: #ffffff; font-size: 36px; }
  .product-list {
    position: absolute; left: 0; right: 0; bottom: 34px;
    list-style: none; display: flex; justify-content: center; gap: 12px;
    font-weight: 700; font-size: 13px; color: var(--ink-light);
  }
  .product-list li { display: flex; align-items: center; gap: 5px; }
  .product-list li::before {
    content: ""; width: 6px; height: 6px; border-radius: 50%;
    background: var(--brand-green);
  }
</style>
</head>
<body>
<main class="canvas">
  <section class="card card--front">
    <div class="front__decor" role="img" aria-label="Faint brand emblem decoration"></div>
    <div class="front__person">
      <p class="person__name">Daniel Marsh</p>
      <p class="person__role">Manager</p>
    </div>
    <div class="front__brand">
      <span class="brand-dot"></span>
      <div>
        <p class="brand-name">Birchwood Clover</p>
        <ul class="contact-list">
          <li>
            <svg class="contact-icon" viewBox="0 0 24 24" aria-hidden="true">
              <path fill="#00a14b" d="M6.6 10.8a15.1 15.1 0 0 0 6.6 6.6l2.2-2.2a1 1 0 0 1 1-.25 11.4 11.4 0 0 0 3.6.57 1 1 0 0 1 1 1V20a1 1 0 0 1-1 1A17 17 0 0 1 3 4a1 1 0 0 1 1-1h3.5a1 1 0 0 1 1 1c0 1.25.2 2.45.57 3.6a1 1 0 0 1-.25 1z"/>
            </svg>
            555-218-3946
          </li>
          <li><span class="contact-square"></span>@birchwoodclover</li>
        </ul>
      </div>
    </div>
  </section>

  <section class="card card--back">
    <div class="back__brand">
      <span class="brand-dot"></span>
      <p class="brand-name">Birchwood Clover</p>
    </div>
    <ul class="product-list">
      <li>Orchardgrass Hay</li>
      <li>Alfalfa Hay</li>
      <li>Mixed Grass Hay</li>
      <li>Premium Quality Hay</li>
    </ul>
  </section>
</main>
</body>
</html>
```